Health and Wellness company needs flyer to promote free seminar

Stride reform studio is a health and wellness company that offers an exercise program designed by physical therapists to help relieve pain and improve mobility. Our business is a new concept that is not well understood by the public. In order to promote our business we offer a free seminar where we present information regarding the underlying cause of pain and tightness. During the seminar we also perform a posture screen and movement testing for all participants.

Target Market(s)

Mostly healthy and active women ages 25-65

Industry/Entity Type

Health And Wellness

Font styles to use
Sans Serif

Colors

Designer to choose colors to be used in the design.

Requirements
Must have
• Title: Eliminate Pain and Tightness For Good
• Paragraph: Stride Reform Studio offers a free 60 minute seminar: "The Busy Walker's Handbook to Bending and Standing Taller."
• What to Expect:
• • Identify the underlying cause of your pain and mobility issues
• • Expose what gets in the way of you moving and feeling better
• • Learn why traditional exercises don’t help and can actually make the problem worse
• • Reveal what your posture is saying and how that impacts you
• • Experience your muscle imbalances through movement tests
• • Discover the training method that realigns your posture, increases your mobility and reduces your pain
• Call to action: RSVP online at stridereformstudio.com
Nice to have
• Use a relevant image showing a female dealing with tightness in the low back, legs, etc.
• Emphasize that the seminar is FREE.
• Make the call to action prominent.

```html
<!DOCTYPE html>
<html lang="en">
<head>
<meta charset="utf-8">
<title>Free Seminar Flyer – Stride Reform Studio</title>
<link rel="stylesheet" href="https://fonts.googleapis.com/css2?family=Montserrat:wght@300;400;500;600;800&family=Oswald:wght@400;600&family=Roboto+Condensed:wght@400;700&family=Open+Sans:wght@400;600&display=swap">
<style>
  :root{
    --orange:#f2901c;
    --purple:#4a17c9;
    --panel:#6a6a6a;
    --band:#4d4d4d;
    --ink:#1c1c1c;
    --quote:#3a3a3a;
    --page:#eef0f2;
    --white:#ffffff;
  }
  *{margin:0;padding:0;box-sizing:border-box}
  html,body{width:1200px;height:1200px;overflow:hidden;background:var(--page)}
  .flyer{position:absolute;left:167px;top:40px;width:866px;height:1120px;background:var(--white);overflow:hidden;box-shadow:0 10px 30px rgba(0,0,0,.12)}
  .shapes{position:absolute;inset:0}
  .brand{position:absolute;right:70px;top:48px;display:flex;align-items:center;gap:12px}
  .brand-mark{width:34px;height:34px;border:4px solid var(--purple)}
  .brand-name{font:600 28px "Montserrat",sans-serif;color:var(--purple);letter-spacing:-.3px}
  .badge{position:absolute;left:445px;top:180px;width:200px;height:180px;text-align:center;color:var(--white);transform:rotate(-8deg)}
  .badge-free{font:600 66px/1 "Oswald",sans-serif;margin-top:22px;display:block}
  .badge-seminar{font:800 30px/1 "Montserrat",sans-serif;color:var(--ink);display:block;margin-top:6px}
  .headline{position:absolute;left:34px;top:456px;width:440px}
  .headline-top{font:400 50px/1 "Oswald",sans-serif;color:var(--ink);display:block}
  .headline-main{font:600 96px/1.05 "Oswald",sans-serif;color:var(--orange);display:block;margin-top:2px}
  .headline-end{font:300 72px/1 "Montserrat",sans-serif;color:var(--purple);display:block;margin-top:0}
  .offer{position:absolute;left:34px;top:718px;width:440px}
  .offer-lead{font:800 21px/1.3 "Montserrat",sans-serif;color:var(--orange)}
  .offer-title{font:700 30px/1.15 "Roboto Condensed",sans-serif;color:var(--quote);margin-top:8px}
  .cta{position:absolute;left:34px;top:878px;width:440px}
  .cta-block{padding:8px 0 10px}
  .cta-block + .cta-block{border-top:1.5px solid #8a8a8a;margin-top:6px;padding-top:14px}
  .cta-label{font:600 28px/1.15 "Montserrat",sans-serif;color:var(--purple)}
  .cta-url{font:400 27px/1.2 "Roboto Condensed",sans-serif;color:var(--ink)}
  .expect{position:absolute;left:580px;top:392px;width:270px;color:var(--white)}
  .expect-heading{font:500 33px/1 "Montserrat",sans-serif;margin-bottom:20px}
  .expect-heading span{color:var(--orange)}
  .expect-list{list-style:none}
  .expect-item{height:90px;border-bottom:1px solid rgba(255,255,255,.75);margin-bottom:10px;padding-top:4px}
  .expect-item:last-child{border-bottom:none;margin-bottom:0}
  .expect-title{font:500 19px/1.1 "Montserrat",sans-serif;color:var(--orange)}
  .expect-text{font:400 13px/1.3 "Open Sans",sans-serif;margin-top:4px}
  .footer-url{position:absolute;left:0;right:0;bottom:26px;text-align:center;font:400 13px "Open Sans",sans-serif;letter-spacing:5px;color:var(--white)}
</style>
</head>
<body>
<article class="flyer">
  <svg class="shapes" width="866" height="1120" viewBox="0 0 866 1120">
    <defs>
      <linearGradient id="photoTone" x1="0" y1="0" x2="1" y2="1">
        <stop offset="0" stop-color="#c9cdd2"/>
        <stop offset=".5" stop-color="#6b6f75"/>
        <stop offset="1" stop-color="#2a2a2e"/>
      </linearGradient>
      <linearGradient id="classTone" x1="0" y1="0" x2="0" y2="1">
        <stop offset="0" stop-color="#ffffff"/>
        <stop offset=".35" stop-color="#e4e4e6"/>
        <stop offset="1" stop-color="#d6d6d8"/>
      </linearGradient>
      <radialGradient id="badgeRing" cx=".5" cy=".4" r=".6">
        <stop offset="0" stop-color="#ffffff"/>
        <stop offset="1" stop-color="#a9a9a9"/>
      </radialGradient>
    </defs>
    <polygon points="0,110 450,110 450,290 0,460" fill="url(#photoTone)" role="img" aria-label="Photo: woman in pink training with a dumbbell in a gym"/>
    <line x1="0" y1="462" x2="450" y2="292" stroke="var(--orange)" stroke-width="5"/>
    <polygon points="0,700 520,610 520,1060 0,1060" fill="url(#classTone)" opacity=".8" role="img" aria-label="Faded photo of a group fitness class"/>
    <polygon points="520,360 866,170 866,1060 520,1060" fill="var(--panel)"/>
    <line x1="300" y1="110" x2="470" y2="205" stroke="var(--purple)" stroke-width="5"/>
    <line x1="625" y1="245" x2="866" y2="130" stroke="var(--purple)" stroke-width="5"/>
    <rect x="0" y="1060" width="866" height="60" fill="var(--band)"/>
    <circle cx="545" cy="270" r="108" fill="url(#badgeRing)"/>
    <circle cx="545" cy="270" r="92" fill="var(--orange)"/>
    <g stroke-width="3" fill="var(--orange)">
      <g transform="translate(520,488)"><circle r="34" stroke="var(--purple)"/><circle r="30" stroke="var(--white)" stroke-width="2" fill="none"/>
        <circle cx="4" cy="-4" r="9" stroke="var(--white)" fill="none"/><line x1="-3" y1="3" x2="-13" y2="13" stroke="var(--white)"/></g>
      <g transform="translate(520,588)"><circle r="34" stroke="var(--purple)"/><circle r="30" stroke="var(--white)" stroke-width="2" fill="none"/>
        <path d="M-10 4 L0 -8 L10 4 M-6 3 V12 H6 V3" stroke="var(--white)" fill="none"/></g>
      <g transform="translate(520,688)"><circle r="34" stroke="var(--purple)"/><circle r="30" stroke="var(--white)" stroke-width="2" fill="none"/>
        <path d="M-12 12 V-6 H12 V12 Z M-12 -6 L0 -14 L12 -6" stroke="var(--white)" fill="none"/></g>
      <g transform="translate(520,788)"><circle r="34" stroke="var(--purple)"/><circle r="30" stroke="var(--white)" stroke-width="2" fill="none"/>
        <path d="M0 -14 V4 M-7 -6 L0 -14 L7 -6 M-12 10 H12" stroke="var(--white)" fill="none"/></g>
      <g transform="translate(520,888)"><circle r="34" stroke="var(--purple)"/><circle r="30" stroke="var(--white)" stroke-width="2" fill="none"/>
        <path d="M-10 -13 H10 V13 H-10 Z M-5 -4 L-2 -1 L5 -8 M-5 6 H5" stroke="var(--white)" fill="none"/></g>
      <g transform="translate(520,988)"><circle r="34" stroke="var(--purple)"/><circle r="30" stroke="var(--white)" stroke-width="2" fill="none"/>
        <path d="M-2 0 H2" stroke="var(--white)"/><circle cx="-8" cy="0" r="6" stroke="var(--white)" fill="none"/><circle cx="8" cy="0" r="6" stroke="var(--white)" fill="none"/></g>
    </g>
  </svg>

  <div class="brand">
    <span class="brand-mark"></span>
    <span class="brand-name">Stride Reform Studio</span>
  </div>

  <div class="badge">
    <span class="badge-free">FREE</span>
    <span class="badge-seminar">SEMINAR</span>
  </div>

  <h1 class="headline">
    <span class="headline-top">ELIMINATE PAIN &amp;</span>
    <span class="headline-main">TIGHTNESS</span>
    <span class="headline-end">FOR GOOD</span>
  </h1>

  <section class="offer">
    <p class="offer-lead">Stride Reform Studio Offers<br>A Free 60 Minute Seminar:</p>
    <p class="offer-title">"The Busy Walker's Handbook to<br>Bending and Standing Taller."</p>
  </section>

  <section class="cta">
    <div class="cta-block">
      <p class="cta-label">Sign up online at :</p>
      <p class="cta-url">stridereformstudio.com/free-seminar</p>
    </div>
    <div class="cta-block">
      <p class="cta-label">RSVP online at :</p>
      <p class="cta-url">stridereformstudio.com</p>
    </div>
  </section>

  <section class="expect">
    <h2 class="expect-heading">What to <span>Expect</span></h2>
    <ul class="expect-list">
      <li class="expect-item"><p class="expect-title">Identify</p><p class="expect-text">the underlying cause of your pain and mobility issues</p></li>
      <li class="expect-item"><p class="expect-title">Expose</p><p class="expect-text">what gets in the way of you moving and feeling better</p></li>
      <li class="expect-item"><p class="expect-title">Learn</p><p class="expect-text">why traditional exercises don't help and can actually make the problem worse</p></li>
      <li class="expect-item"><p class="expect-title">Reveal</p><p class="expect-text">what your posture is saying and how that impacts you</p></li>
      <li class="expect-item"><p class="expect-title">Experience</p><p class="expect-text">your muscle imbalances through movement tests</p></li>
      <li class="expect-item"><p class="expect-title">Discover</p><p class="expect-text">the training method that realigns your posture, increases your mobility and reduces your pain</p></li>
    </ul>
  </section>

  <p class="footer-url">www.stridereformstudio.com</p>
</article>
</body>
</html>
```